Visitenkarten-Design für Yogakurse
Zielgruppe
Ich biete Yogakurse für alle an sowieso speziell Yogakurse für Schwangere, frischgebackene Mamas und Rückbildungskurse.
Meine Zielgruppe sind hauptsächlich schwangere Frauen sowieso Frauen mit Babys.
Aufgabenstellung
Folgende Informationen sollten enthalten sein:
Ruhe im Atem
Yoga & Beckenbodentraining
Henrike Wolmsen
info@ruhe-im-atem-beispiel.de
www.ruhe-im-atem-beispiel.de

```html
<!DOCTYPE html>
<html lang="de">
<head>
<meta charset="utf-8">
<title>Ruhe im Atem – Visitenkarte</title>
<link rel="stylesheet" href="https://fonts.googleapis.com/css2?family=Montserrat:wght@400;500&family=Caveat+Brush&display=swap">
<style>
  :root {
    --backdrop: #c8c8c8;
    --card: #e4e8dc;
    --arc: #b88c72;
    --arc-halo: #d3e2c6;
    --gold: #b8862e;
    --rose-brown: #b08a78;
    --sage: #a9c79a;
  }
  * { box-sizing: border-box; margin: 0; padding: 0; }
  html, body {
    width: 1200px; height: 800px; overflow: hidden;
    background: var(--backdrop);
  }
  .canvas { position: relative; width: 1200px; height: 800px; }

  .card {
    position: absolute;
    top: 337px;
    width: 480px; height: 277px;
    background: var(--card);
    overflow: hidden;
  }
  .card--front { left: 97px; }
  .card--back  { left: 612px; }

  .card__arcs { position: absolute; inset: 0; width: 100%; height: 100%; }
  .card__arcs .halo { fill: none; stroke: var(--arc-halo); stroke-width: 9; }
  .card__arcs .line { fill: none; stroke: var(--arc); stroke-width: 4.5; }

  /* Front */
  .brand {
    position: absolute; left: 0; right: 0; top: 118px;
    display: flex; justify-content: center; align-items: center; gap: 10px;
    font-family: "Montserrat", sans-serif;
    font-weight: 500; font-size: 26px; color: var(--gold);
  }
  .brand__dot {
    width: 14px; height: 14px; border-radius: 50%;
    background: var(--gold);
  }
  .front__rule {
    position: absolute; left: 141px; width: 243px; top: 174px;
    height: 1.5px; background: var(--sage);
  }
  .front__tagline {
    position: absolute; left: 78px; top: 190px;
    font-family: "Caveat Brush", cursive;
    font-size: 30px; letter-spacing: 2.5px; color: var(--gold);
    white-space: nowrap;
  }

  /* Back */
  .person { position: absolute; left: 8px; top: 48px; color: var(--rose-brown); font-family: "Montserrat", sans-serif; }
  .person__name { font-weight: 500; font-size: 23px; white-space: nowrap; }
  .person__role { font-weight: 400; font-size: 13px; margin-top: 6px; }

  .back__divider {
    position: absolute; left: 243px; top: 28px;
    width: 2px; height: 222px; background: var(--arc);
  }
  .contact {
    position: absolute; left: 258px; top: 137px;
    list-style: none;
    font-family: "Montserrat", sans-serif; font-size: 11.5px;
    color: var(--rose-brown);
  }
  .contact__item { display: flex; align-items: center; gap: 7px; height: 28.5px; white-space: nowrap; }
  .contact__icon { width: 12px; height: 12px; flex: none; fill: var(--gold); }
  .contact__icon--stroke { fill: none; stroke: var(--gold); stroke-width: 1.3; }
</style>
</head>
<body>
<main class="canvas">

  <section class="card card--front" aria-label="Vorderseite">
    <svg class="card__arcs" viewBox="0 0 480 277" aria-hidden="true">
      <path class="halo" d="M312 -2 Q420 45 480 122"/>
      <path class="line" d="M312 -2 Q420 45 480 120"/>
      <path class="halo" d="M6 163 Q70 245 162 279"/>
      <path class="line" d="M7 165 Q70 245 160 279"/>
    </svg>
    <div class="brand"><span class="brand__dot"></span><span class="brand__name">Ruhe im Atem</span></div>
    <div class="front__rule"></div>
    <p class="front__tagline">Yoga &amp; Beckenbodentraining</p>
  </section>

  <section class="card card--back" aria-label="Rückseite">
    <svg class="card__arcs" viewBox="0 0 480 277" aria-hidden="true">
      <path class="line" d="M312 -2 Q420 45 480 120"/>
      <path class="line" d="M7 165 Q70 245 160 279"/>
    </svg>
    <div class="person">
      <h1 class="person__name">Henrike Wolmsen</h1>
      <p class="person__role">Yoga &amp; Beckenbodentraining</p>
    </div>
    <div class="back__divider"></div>
    <ul class="contact">
      <li class="contact__item">
        <svg class="contact__icon" viewBox="0 0 24 24" aria-hidden="true"><path d="M6.6 10.8a15.1 15.1 0 0 0 6.6 6.6l2.2-2.2a1 1 0 0 1 1-.25 11.4 11.4 0 0 0 3.6.57 1 1 0 0 1 1 1V20a1 1 0 0 1-1 1A17 17 0 0 1 3 4a1 1 0 0 1 1-1h3.5a1 1 0 0 1 1 1c0 1.25.2 2.45.57 3.57a1 1 0 0 1-.25 1z"/></svg>
        <span>0170 - 4839216</span>
      </li>
      <li class="contact__item">
        <svg class="contact__icon" viewBox="0 0 24 24" aria-hidden="true"><path d="M2 5h20v14H2z"/><path d="M2 5l10 7 10-7" fill="none" stroke="#e4e8dc" stroke-width="2"/></svg>
        <span>info@ruhe-im-atem-beispiel.de</span>
      </li>
      <li class="contact__item">
        <svg class="contact__icon contact__icon--stroke" viewBox="0 0 24 24" aria-hidden="true"><circle cx="12" cy="12" r="10"/><ellipse cx="12" cy="12" rx="4.5" ry="10"/><path d="M2 12h20M4 7h16M4 17h16"/></svg>
        <span>www.ruhe-im-atem-beispiel.de</span>
      </li>
    </ul>
  </section>

</main>
</body>
</html>
```